Event Graphics for a Summer Camp for Middle School and High School Students

I need graphics designed for our summer camps event. These camps are for teenagers, 6-12th grades. Primary graphic design is for a 11x17 poster but will also need the images resized for:
-social media
-16x9 title slide
- a postcard size
Graphic should include the following:
-Main Title: RV Pathlight presents . . . Summer Camp
-Dates: Kindle - June 3-7, High School - June 8-12, Middle School - June 22-26
-Register at RVPathlight.com
-Maple Crest Retreat Center, Deadwood, SD
-For each camp, include name and headshot of speaker: Kindle: Tom Wakeley (black jacket photo), High: Luis Ortega (hispanic man), Middle: Barrington Pope (tan shirt). Gave some options for headshots. Use what works best for cropping.
-Include RV Pathlight logo
-Event Graphic should be attractive to teenagers. Open to ideas
My graphic design experience is limited. I will need help receiving the files I need in the various sizes. Thank you.

```html
<!DOCTYPE html>
<html lang="en">
<head>
<meta charset="utf-8">
<title>RV Pathlight Summer Camp</title>
<link rel="stylesheet" href="https://fonts.googleapis.com/css2?family=Poppins:wght@500&family=Oswald:wght@400&family=Amatic+SC:wght@700&display=swap">
<style>
  :root {
    --sky: #5ef2dc;
    --scene-top: #3f9c8a;
    --scene-bottom: #2a6a84;
    --frame: #e8ff1c;
    --panel: #2f7f86;
    --ink: #111111;
    --photo: #2e3a3c;
    --location-bg: rgba(205, 215, 232, 0.62);
  }
  * { margin: 0; padding: 0; box-sizing: border-box; }
  html, body { width: 776px; height: 1200px; overflow: hidden; }
  body { background: var(--sky); font-family: "Poppins", sans-serif; color: var(--ink); }
  .poster { position: relative; width: 776px; height: 1200px; overflow: hidden; background: var(--sky); }

  .scene { position: absolute; inset: 0; }

  .headline { position: absolute; left: 22px; top: 22px; font-size: 46px; font-weight: 500; letter-spacing: -1px; line-height: 1; }
  .subtitle { position: absolute; left: 26px; top: 90px; font-family: "Amatic SC", cursive; font-size: 44px; line-height: 1; }

  .camp-frame { position: absolute; border: 9px solid var(--frame); }
  .camp-frame .inner-line { position: absolute; background: var(--frame); }

  .band { position: absolute; background: var(--frame); display: flex; align-items: center; justify-content: center; text-align: center; line-height: 1; }
  .band.dates { font-size: 38px; font-weight: 500; }
  .condensed { font-family: "Oswald", sans-serif; letter-spacing: -1px; }

  .headshot { position: absolute; border: 2px solid var(--frame); background: linear-gradient(160deg, #3b4a4c, var(--photo)); }

  .location { position: absolute; left: 485px; top: 873px; width: 291px; height: 172px; background: var(--location-bg); font-size: 27px; font-weight: 500; line-height: 1.45; text-align: center; padding-top: 14px; letter-spacing: -0.5px; }
  .register { position: absolute; left: 0; width: 776px; top: 1143px; text-align: center; font-size: 30px; font-weight: 500; letter-spacing: -0.5px; }
</style>
</head>
<body>
<div class="poster">

  <svg class="scene" width="776" height="1200" viewBox="0 0 776 1200" role="img" aria-label="Illustrated night campsite with mountains, moon, stars and a red tent">
    <defs>
      <linearGradient id="night" x1="0" y1="0" x2="0" y2="1">
        <stop offset="0" stop-color="var(--scene-top)"/>
        <stop offset="1" stop-color="var(--scene-bottom)"/>
      </linearGradient>
    </defs>
    <path d="M0 215 L776 92 L776 1125 Q388 1175 0 1125 Z" fill="url(#night)"/>
  </svg>

  <div class="headline">RV Pathlight presents</div>
  <div class="subtitle">Summer Camp</div>

  <!-- Kindle camp -->
  <div class="camp-frame" style="left:54px;top:190px;width:296px;height:458px;">
    <span class="inner-line" style="left:80px;top:0;width:3px;height:60px"></span>
    <span class="inner-line" style="left:200px;top:0;width:3px;height:60px"></span>
  </div>
  <div class="band condensed" style="left:54px;top:232px;width:296px;height:116px;font-size:44px;transform:rotate(2deg);">Kindle - June 3-7</div>
  <div class="headshot" style="left:150px;top:348px;width:115px;height:119px;" role="img" aria-label="Headshot of speaker Tom Wakeley in a black jacket"></div>
  <div class="band" style="left:22px;top:478px;width:368px;height:112px;transform:rotate(-2deg);font-size:50px;justify-content:flex-start;padding-left:12px;">Speaker:<span class="condensed" style="font-size:34px;margin-left:4px;">Tom Wakeley</span></div>

  <!-- Middle school camp -->
  <div class="camp-frame" style="left:424px;top:187px;width:296px;height:457px;">
    <span class="inner-line" style="left:90px;top:0;width:3px;height:50px"></span>
    <span class="inner-line" style="left:200px;top:0;width:3px;height:50px"></span>
  </div>
  <div class="band dates" style="left:430px;top:224px;width:338px;height:118px;flex-direction:column;transform:rotate(-2deg);">Middle School<br>June 22-26</div>
  <div class="headshot" style="left:525px;top:342px;width:118px;height:120px;" role="img" aria-label="Headshot of speaker Barrington Pope in a tan shirt"></div>
  <div class="band" style="left:400px;top:470px;width:368px;height:118px;transform:rotate(2deg);font-size:50px;"><span class="condensed" style="font-size:34px;margin-right:8px;">Barrington</span>Pope</div>

  <!-- High school camp -->
  <div class="camp-frame" style="left:146px;top:668px;width:297px;height:457px;">
    <span class="inner-line" style="left:144px;bottom:0;width:3px;height:55px"></span>
    <span class="inner-line" style="left:0;bottom:55px;width:279px;height:3px"></span>
  </div>
  <div class="band dates" style="left:124px;top:738px;width:342px;height:116px;flex-direction:column;transform:rotate(-3deg);">High School<br>June 8-12</div>
  <div class="headshot" style="left:222px;top:858px;width:120px;height:120px;" role="img" aria-label="Headshot of speaker Luis Ortega holding a gift"></div>
  <div class="band" style="left:155px;top:984px;width:288px;height:100px;transform:rotate(3deg);font-size:50px;"><span class="condensed" style="font-size:34px;margin-right:8px;">Luis</span>Ortega</div>

  <div class="location">Maple Crest Retreat<br>Center,<br>Deadwood, SD</div>

  <div class="register">Register at RVPathlight.com</div>
</div>
</body>
</html>
```